Women's Health Company needs business card

We need a business card for a USA based women's health care company. We use digital technology to enhance therapy prescribed by clinicians for their patients

```html
<!DOCTYPE html>
<html lang="en">
<head>
<meta charset="UTF-8">
<title>Lunova Health – Business Card</title>
<link href="https://fonts.googleapis.com/css2?family=Poppins:wght@400;600&display=swap" rel="stylesheet">
<style>
  :root {
    --backdrop: #2b2b2d;
    --card: #1c1d1f;
    --teal: #74c5bd;
    --purple: #9b59b6;
    --ink: #ffffff;
    --rule: #7a7b7e;
    --pattern-dark: #222325;
    --pattern-light: #3a3b3e;
  }
  * { margin: 0; padding: 0; box-sizing: border-box; }
  html, body {
    width: 1200px; height: 1108px; overflow: hidden;
    background: var(--backdrop);
    font-family: "Poppins", sans-serif;
  }
  .stage {
    position: relative; width: 1200px; height: 1108px;
    display: flex; justify-content: center; align-items: center; gap: 60px;
  }
  .card {
    position: relative; width: 420px; height: 640px;
    background: var(--card); border-radius: 20px;
    box-shadow: 0 14px 30px rgba(0,0,0,.45);
    overflow: hidden;
  }
  .card-front {
    display: flex; flex-direction: column; align-items: center;
    padding-top: 125px; text-align: center;
  }
  .brand {
    display: flex; align-items: center; gap: 10px;
    color: var(--teal); font-weight: 400; font-size: 42px;
    line-height: 1; white-space: nowrap;
  }
  .brand-dot { flex: none; width: 11px; height: 11px; border-radius: 50%; background: var(--purple); }
  .holder-name {
    margin-top: 110px; color: var(--teal); font-weight: 600; font-size: 26px;
    line-height: 1.3; text-transform: uppercase; letter-spacing: .5px;
  }
  .holder-role { color: var(--purple); font-size: 17px; line-height: 1.4; }
  .icon-row {
    display: flex; align-items: center; gap: 8px; margin-top: 14px;
    width: 300px;
  }
  .icon-row::before, .icon-row::after {
    content: ""; flex: 1; height: 1px; background: var(--rule);
  }
  .icon-box {
    width: 26px; height: 26px; border-radius: 4px; background: var(--teal);
    display: flex; align-items: center; justify-content: center;
  }
  .contact-list { list-style: none; margin-top: 10px; color: var(--ink); font-size: 18px; line-height: 1.4; }
  .divider { flex: none; width: 300px; height: 1px; background: var(--rule); margin: 16px 0 12px; }
  .address { color: var(--ink); font-size: 17px; line-height: 1.4; font-style: normal; }
  .pattern-field {
    position: absolute; inset: 0;
    background: linear-gradient(160deg, var(--pattern-light) 0%, var(--pattern-dark) 55%, var(--pattern-dark) 100%);
  }
  .back-brand {
    position: absolute; left: 210px; top: 475px;
    color: var(--teal); font-size: 30px; font-weight: 400; line-height: 1;
  }
</style>
</head>
<body>
<main class="stage">
  <section class="card card-front" aria-label="Card front">
    <div class="brand"><span class="brand-name">Lunova Health</span><span class="brand-dot"></span></div>
    <h1 class="holder-name">Marcus Ellery</h1>
    <p class="holder-role">Managing Director</p>
    <div class="icon-row">
      <span class="icon-box">
        <svg width="16" height="16" viewBox="0 0 24 24"><path fill="#1c1d1f" d="M6.6 10.8a15.1 15.1 0 0 0 6.6 6.6l2.2-2.2c.3-.3.7-.4 1-.2 1.1.4 2.3.6 3.6.6.6 0 1 .4 1 1V20c0 .6-.4 1-1 1A17 17 0 0 1 3 4c0-.6.4-1 1-1h3.5c.6 0 1 .4 1 1 0 1.3.2 2.5.6 3.6.1.3 0 .7-.2 1z"/></svg>
      </span>
      <span class="icon-box">
        <svg width="16" height="16" viewBox="0 0 24 24"><rect x="3" y="5" width="18" height="14" rx="1" fill="none" stroke="#1c1d1f" stroke-width="2"/><path d="M3 6l9 7 9-7" fill="none" stroke="#1c1d1f" stroke-width="2"/></svg>
      </span>
      <span class="icon-box">
        <svg width="16" height="16" viewBox="0 0 24 24"><circle cx="12" cy="12" r="9" fill="none" stroke="#1c1d1f" stroke-width="2"/><path d="M3 12h18M12 3c3 3 3 15 0 18M12 3c-3 3-3 15 0 18" fill="none" stroke="#1c1d1f" stroke-width="1.5"/></svg>
      </span>
    </div>
    <ul class="contact-list">
      <li>044-987 654 321</li>
      <li>hello@lunovacare.com</li>
      <li>www.lunovacare.com</li>
    </ul>
    <div class="divider"></div>
    <address class="address">218 Willow Lane, Suite 4<br>60614, United States</address>
  </section>

  <section class="card card-back" aria-label="Card back">
    <div class="pattern-field" role="img" aria-label="Repeating tone-on-tone brand name pattern with a soft gloss"></div>
    <span class="back-brand">Lunova</span>
  </section>
</main>
</body>
</html>
```